Brochure for High Net Worth Financial Advisory business

I would like to get a brochure designed that has the first few pages discussing our philosophy and process for investing.
We believe that model portfolios that are directly owned by clients and then monitored by our portfolio team are a solution to the opaqueness of managed funds and by then layering protection strategies over the top of these portfolios clients can get a better risk reward outcome.
The brochure would need to include a sleeve at the back in which we can place our paper portfolio documents and a slot for a business card would be appreciated.
We would like to convey strength, security and innovation in finance with our target market being high net worth individuals ($2m+) and other financial institutions.
Target Market(s)
High net worth investing clients, financial institutions
Industry/Entity Type
Financial
Requirements
Must have
- The text that included - diagrams if they suit
A sleeve for A4 paper
A holder for business cards
Nice to have
- Out logo is on the first page, with our catch line, it would be nice to incorporate this within the document

```html
<!DOCTYPE html>
<html lang="en">
<head>
<meta charset="utf-8">
<title>Meridian Crest Advisory — Brochure Cover</title>
<link rel="stylesheet" href="https://fonts.googleapis.com/css2?family=Cinzel:wght@400&family=Arimo:wght@400;700&display=swap">
<style>
  :root {
    --navy-deep: #070f4a;
    --navy: #0b1f7a;
    --blue: #1455b5;
    --blue-bright: #1f86d6;
    --cyan: #35b7ef;
    --silver-light: #f2f4f8;
    --silver-dark: #8b93a6;
    --white: #ffffff;
    --glow: #7fe3f2;
    --gap: #ffffff;
  }
  html, body {
    margin: 0;
    padding: 0;
    width: 1200px;
    height: 423px;
    overflow: hidden;
    background: var(--gap);
  }
  .spread {
    position: relative;
    width: 1200px;
    height: 423px;
    display: flex;
    justify-content: space-between;
    background: var(--gap);
  }
  .panel {
    position: relative;
    height: 423px;
    overflow: hidden;
    background:
      linear-gradient(160deg, var(--blue-bright) 0%, var(--blue) 35%, var(--navy) 70%, var(--navy-deep) 100%);
  }
  .panel--back { width: 596px; }
  .panel--front { width: 598px; }
  .panel__art {
    position: absolute;
    inset: 0;
    width: 100%;
    height: 100%;
  }
  .back-contact {
    position: absolute;
    left: 0;
    width: 596px;
    bottom: 14px;
    text-align: center;
    color: var(--white);
    font-family: "Arimo", Arial, sans-serif;
    font-size: 12px;
    line-height: 14px;
    font-weight: 700;
  }
  .back-contact__name {
    font-family: "Cinzel", "Times New Roman", serif;
    font-weight: 400;
    font-size: 10px;
    letter-spacing: 0.5px;
    color: var(--silver-light);
    margin-bottom: 10px;
  }
  .back-contact__line { display: block; }
  .back-contact__phone,
  .back-contact__email { color: var(--cyan); }
  .back-contact__web {
    display: inline-block;
    margin-top: 2px;
    padding: 0 6px;
    background: var(--cyan);
    color: var(--white);
    border-radius: 4px;
  }
  .front-brand {
    position: absolute;
    left: 0;
    width: 598px;
    top: 322px;
    text-align: center;
    color: var(--silver-light);
  }
  .front-brand__name {
    font-family: "Cinzel", "Times New Roman", serif;
    font-size: 26px;
    letter-spacing: 1px;
    margin: 0;
    line-height: 30px;
  }
  .front-brand__tagline {
    margin: 10px 0 0;
    font-family: "Arimo", Arial, sans-serif;
    font-size: 8px;
    color: var(--white);
  }
</style>
</head>
<body>
<main class="spread">

  <section class="panel panel--back" aria-label="Back cover">
    <svg class="panel__art" viewBox="0 0 596 423" aria-hidden="true">
      <g fill="#5ec2f5" opacity="0.12">
        <rect x="-40" y="-60" width="60" height="420" rx="8" transform="rotate(-38 0 0)"/>
        <rect x="120" y="-120" width="90" height="520" rx="10" transform="rotate(-38 160 140)"/>
        <rect x="260" y="-80" width="50" height="480" rx="8" transform="rotate(-38 280 160)"/>
        <rect x="380" y="-40" width="110" height="520" rx="12" transform="rotate(-38 430 220)"/>
      </g>
      <g fill="#8fd6ff" opacity="0.08">
        <rect x="60" y="-100" width="24" height="500" transform="rotate(-38 70 150)"/>
        <rect x="320" y="-60" width="20" height="520" transform="rotate(-38 330 200)"/>
      </g>
    </svg>
    <div class="back-contact">
      <div class="back-contact__name">Meridian Crest Advisory</div>
      <span class="back-contact__line">Meridian Crest Advisory</span>
      <span class="back-contact__line">14 Harbour Row, Sydney NSW 2000</span>
      <span class="back-contact__line back-contact__phone">+61 2 5550 0142</span>
      <span class="back-contact__line back-contact__email">info@meridiancrest.com</span>
      <span class="back-contact__web">meridiancrest.com</span>
    </div>
  </section>

  <section class="panel panel--front" aria-label="Front cover">
    <svg class="panel__art" viewBox="0 0 598 423">
      <defs>
        <linearGradient id="top-band" x1="0" y1="0" x2="1" y2="0">
          <stop offset="0" stop-color="#0a1a66"/>
          <stop offset="0.55" stop-color="#071050"/>
          <stop offset="1" stop-color="#06093a"/>
        </linearGradient>
        <radialGradient id="photo-glow" cx="0.55" cy="0.35" r="0.6">
          <stop offset="0" stop-color="#bff3f7"/>
          <stop offset="0.35" stop-color="#3fb6d8"/>
          <stop offset="0.75" stop-color="#0d3a7a"/>
          <stop offset="1" stop-color="#071050" stop-opacity="0"/>
        </radialGradient>
        <linearGradient id="silver" x1="0" y1="0" x2="1" y2="0">
          <stop offset="0" stop-color="#9aa3b6"/>
          <stop offset="0.4" stop-color="#f4f6fa"/>
          <stop offset="0.75" stop-color="#b7bfcf"/>
          <stop offset="1" stop-color="#eef1f6"/>
        </linearGradient>
        <clipPath id="above-curve">
          <path d="M0,0 H598 V250 C560,252 470,232 390,190 C270,115 150,62 0,110 Z"/>
        </clipPath>
      </defs>

      <g fill="#5ec2f5" opacity="0.12">
        <rect x="40" y="-60" width="70" height="560" rx="10" transform="rotate(-38 80 200)"/>
        <rect x="230" y="-40" width="100" height="560" rx="12" transform="rotate(-38 280 220)"/>
        <rect x="420" y="0" width="60" height="520" rx="8" transform="rotate(-38 450 250)"/>
      </g>

      <g clip-path="url(#above-curve)">
        <rect x="0" y="0" width="598" height="260" fill="url(#top-band)"/>
        <rect role="img" aria-label="Photograph of open hands holding a glowing miniature city skyline"
              x="330" y="0" width="268" height="250" fill="url(#photo-glow)"/>
      </g>

      <path d="M0,118 C150,70 270,123 390,198 C470,240 560,258 598,258 L598,272 C550,272 460,254 380,212 C260,140 150,92 0,138 Z"
            fill="var(--blue-bright)" opacity="0.9"/>
      <path d="M0,110 C150,62 270,115 390,190 C470,232 560,252 598,250"
            fill="none" stroke="url(#silver)" stroke-width="5"/>
    </svg>

    <div class="front-brand">
      <h1 class="front-brand__name">Meridian Crest Advisory</h1>
      <p class="front-brand__tagline">“Providing comprehensive, innovative and pro-active research, advice, and investment management services”</p>
    </div>
  </section>

</main>
</body>
</html>
```